Mobile Interface Design

Take an existing website design and create a Mobile interface that is creative and easy to navigate. Background programming and stuff already accomplished... need a Graphic Designer with Mobile UI expertise. Need it done quickly in 1-2 weeks.
Go to http://demo.fairwaypulse.example. Signup using invitation code "vinodvisitor" - we need the pick players screen designed for a mobile platform. We have some ideas regarding the layout of the screen. I will upload a mockup. We need to stick to current design site as much as possible but also provide a better mobile site experience.
Notes of the attached file:
The header will have Teebeacon logo, Messages icon, Points and menu (lines).
Ignore second bar
Tournament Info will be a scroll down box (mobile expand layer)
Tokens bar will have the tokens from the web page 100/40
The field - will be the players from the website - will show rank, photo, name, token value (20) and a check box - to select. the check box will change the color of the layer. At the top - the filters will be similar to filters on website. There will be a clear/show selected button to filter list (not required to show on design) - at bottom "Next Choose Winner" button.
We need footer with menu links "Pick Players", "My Beacon", My Games", "My Profile".
If you have any specific questions, please let me know before starting on it.
Updates
This is not a contest for everyone looking to work on it. If you submit your portfolio and ideas, we will work with them directly on the design/delivery. This is my first time posting a project and didn't realize I created a contest.
Target Market(s)
iOS and Android
Look and feel
Each slider illustrates characteristics of the customer's brand and the style your logo design should communicate.

```html
<!DOCTYPE html>
<html lang="en">
<head>
<meta charset="utf-8">
<title>Teebeacon – Pick Players</title>
<link rel="stylesheet" href="https://fonts.googleapis.com/css2?family=PT+Sans:wght@400;700&display=swap">
<style>
:root{
  --page-bg:#2f4675;
  --status-bg:#1b1d22;
  --app-bg-top:#33487a;
  --app-bg-bottom:#1f2f5a;
  --header-top:#5a6fa2;
  --header-bottom:#3a4f83;
  --navy:#1f3566;
  --navy-text:#1e3260;
  --panel:#eceef3;
  --row-line:#d6dae3;
  --muted:#6a7391;
  --light-bar:#dfe3ec;
  --coin:#e0b84a;
  --coin-text:#8a6a12;
  --white:#ffffff;
  --flag-blue:#1f5fb0;
  --flag-yellow:#f2c500;
}
*{box-sizing:border-box;margin:0;padding:0}
html,body{width:1200px;height:960px;overflow:hidden}
body{background:var(--page-bg);font-family:"PT Sans",sans-serif;position:relative}
.screen{position:absolute;left:0;top:0;width:322px;height:480px;transform-origin:0 0;
  transform:translate(302px,36px) scale(1.855);background:linear-gradient(var(--app-bg-top),var(--app-bg-bottom));overflow:hidden}
.status-bar{height:22px;background:var(--status-bg);color:#e8e8e8;display:flex;align-items:center;padding:0 6px;font-size:12px;letter-spacing:.3px;position:relative}
.status-bar .signal{display:flex;align-items:flex-end;gap:1px;height:9px;margin-right:3px}
.status-bar .signal i{display:block;width:2px;background:#e8e8e8}
.status-bar .lock{position:absolute;left:155px;top:5px}
.status-bar .battery{position:absolute;right:6px;top:7px;width:18px;height:8px;border:1px solid #ddd;border-radius:1px;padding:1px}
.status-bar .battery span{display:block;height:100%;background:#ddd}
.app-header{position:absolute;left:17px;top:22px;width:288px;height:37px;background:linear-gradient(var(--header-top),var(--header-bottom));border-radius:0 0 5px 5px;display:flex;align-items:center}
.brand{color:var(--white);font-size:14px;padding-left:8px;flex:1}
.header-item{height:100%;display:flex;align-items:center;justify-content:center;border-left:1px solid rgba(0,0,0,.18)}
.messages{width:30px;border-left:none}
.points{width:40px;flex-direction:column;color:var(--white)}
.points small{font-size:4px;opacity:.8}
.points b{font-size:8px;font-weight:400}
.menu{width:30px}
.tournament{position:absolute;left:17px;top:64px;width:288px;height:21px;display:flex}
.tournament .label{flex:1;background:var(--light-bar);font-size:7px;color:var(--navy-text);padding-left:8px;line-height:21px;border-radius:2px 0 0 2px}
.tournament .toggle{width:30px;background:var(--navy);display:flex;align-items:center;justify-content:center;border-radius:0 2px 2px 0}
.field-panel{position:absolute;left:17px;top:90px;width:288px;height:347px;background:var(--panel);border-radius:3px;overflow:hidden}
.tokens-bar{height:22px;display:flex;align-items:center;font-size:6.5px;color:var(--navy-text);border-bottom:1px solid var(--row-line);padding-left:8px;position:relative}
.tokens-bar span{position:absolute;top:7px}
.btn{background:var(--navy);color:var(--white);border-radius:2px;font-size:6px;display:flex;align-items:center;justify-content:center}
.tokens-bar .btn{position:absolute;left:187px;top:4px;width:30px;height:12px}
.filters{position:absolute;left:229px;top:4px;width:50px;height:12px;background:#d3d7e0;border:1px solid #c3c8d3;border-radius:2px;font-size:6px;color:var(--muted);display:flex;align-items:center;padding:0 5px;justify-content:space-between}
.player-list{list-style:none}
.player-row{height:42px;position:relative;border-bottom:1px solid var(--row-line);background:linear-gradient(#f1f2f6,#e6e9ef)}
.avatar{position:absolute;left:10px;top:10px;width:20px;height:24px;border:1.5px solid var(--navy);background:linear-gradient(#b08d78,#3c2f2a)}
.coin{position:absolute;left:43px;top:17px;width:11px;height:11px;border-radius:50%;background:var(--coin);color:var(--coin-text);font-size:5px;display:flex;align-items:center;justify-content:center}
.player-name{position:absolute;left:69px;top:7px;font-size:10.5px;color:var(--navy-text)}
.ranking{position:absolute;left:70px;top:23px;font-size:5px;color:var(--muted)}
.stats-link{position:absolute;left:135px;top:23px;font-size:5px;color:var(--navy-text);text-decoration:underline}
.flag{position:absolute;left:199px;top:23px}
.checkbox{position:absolute;left:253px;top:17px;width:13px;height:11px;border-radius:2px;background:var(--white);border:1px solid #cfd3dc;display:flex;align-items:center;justify-content:center}
.player-row.unselected .checkbox{opacity:.45}
.scrollbar{position:absolute;left:281px;top:134px;width:6px;height:42px;background:var(--navy)}
.panel-actions{position:absolute;left:0;bottom:0;width:100%;height:22px;background:var(--panel)}
.panel-actions .clear{position:absolute;left:8px;top:4px;width:28px;height:13px}
.panel-actions .next{position:absolute;right:8px;top:4px;width:77px;height:13px}
.tab-bar{position:absolute;left:17px;top:442px;width:288px;height:38px;display:flex;background:linear-gradient(#3f5488,#2a3e70);border-radius:4px 4px 0 0}
.tab{flex:1;display:flex;flex-direction:column;align-items:center;justify-content:center;gap:3px;color:var(--white);font-size:6.5px;border-left:1px solid rgba(0,0,0,.25)}
.tab:first-child{border-left:none}
</style>
</head>
<body>
<main class="screen">
  <div class="status-bar">
    <span class="signal"><i style="height:2px"></i><i style="height:4px"></i><i style="height:6px"></i><i style="height:8px"></i><i style="height:9px"></i></span>
    MERIDIAN&nbsp;&nbsp;3G
    <svg class="lock" width="9" height="11" viewBox="0 0 9 11"><path d="M2 5V3.5a2.5 2.5 0 0 1 5 0V5" fill="none" stroke="#ddd" stroke-width="1.3"/><rect x="1" y="5" width="7" height="6" rx="1" fill="#ddd"/></svg>
    <span class="battery"><span></span></span>
  </div>

  <header class="app-header">
    <div class="brand">Teebeacon</div>
    <div class="header-item messages">
      <svg width="16" height="11" viewBox="0 0 16 11"><path d="M1 1h9v6H5l-3 2V7H1z" fill="#fff"/><path d="M11 3h4v5h-1v2l-2-2H7V7.5h4z" fill="#fff" opacity=".8"/></svg>
    </div>
    <div class="header-item points"><small>Points</small><b>3420</b></div>
    <div class="header-item menu">
      <svg width="11" height="9" viewBox="0 0 11 9"><rect y="0" width="11" height="2" fill="#fff"/><rect y="3.5" width="11" height="2" fill="#fff"/><rect y="7" width="11" height="2" fill="#fff"/></svg>
    </div>
  </header>

  <section class="tournament">
    <div class="label">Tournament Information</div>
    <div class="toggle"><svg width="11" height="7" viewBox="0 0 11 7"><path d="M1 1l4.5 4.5L10 1" fill="none" stroke="#fff" stroke-width="2"/></svg></div>
  </section>

  <section class="field-panel">
    <div class="tokens-bar">
      <span style="left:8px">TOKENS</span>
      <span style="left:50px">Player: 100</span>
      <span style="left:104px">Backup: 40</span>
      <span style="left:163px">Field</span>
      <div class="btn">Clear</div>
      <div class="filters">Filters <svg width="6" height="4" viewBox="0 0 6 4"><path d="M0 0h6L3 4z" fill="#1e3260"/></svg></div>
    </div>

    <ul class="player-list">
      <li class="player-row selected">
        <div class="avatar" role="img" aria-label="Player portrait photo"></div><div class="coin">20</div>
        <div class="player-name">Bram van Dorne</div><div class="ranking">World Ranking: 42</div><div class="stats-link">Player Statistics</div>
        <svg class="flag" width="13" height="8" viewBox="0 0 13 8"><rect width="13" height="8" fill="var(--flag-blue)"/><rect x="4" width="2" height="8" fill="var(--flag-yellow)"/><rect y="3" width="13" height="2" fill="var(--flag-yellow)"/></svg>
        <div class="checkbox"><svg width="7" height="6" viewBox="0 0 7 6"><path d="M1 3l2 2 3-4" fill="none" stroke="#1e3260" stroke-width="1.4"/></svg></div>
      </li>
      <li class="player-row selected">
        <div class="avatar" role="img" aria-label="Player portrait photo"></div><div class="coin">20</div>
        <div class="player-name">Mats Wilde</div><div class="ranking">World Ranking: 42</div><div class="stats-link">Player Statistics</div>
        <svg class="flag" width="13" height="8" viewBox="0 0 13 8"><rect width="13" height="8" fill="var(--flag-blue)"/><rect x="4" width="2" height="8" fill="var(--flag-yellow)"/><rect y="3" width="13" height="2" fill="var(--flag-yellow)"/></svg>
        <div class="checkbox"><svg width="7" height="6" viewBox="0 0 7 6"><path d="M1 3l2 2 3-4" fill="none" stroke="#1e3260" stroke-width="1.4"/></svg></div>
      </li>
      <li class="player-row selected">
        <div class="avatar" role="img" aria-label="Player portrait photo"></div><div class="coin">20</div>
        <div class="player-name">Rolf Garrison</div><div class="ranking">World Ranking: 42</div><div class="stats-link" style="left:137px">Player Statistics</div>
        <svg class="flag" width="13" height="8" viewBox="0 0 13 8"><rect width="13" height="8" fill="var(--flag-blue)"/><rect x="4" width="2" height="8" fill="var(--flag-yellow)"/><rect y="3" width="13" height="2" fill="var(--flag-yellow)"/></svg>
        <div class="checkbox"><svg width="7" height="6" viewBox="0 0 7 6"><path d="M1 3l2 2 3-4" fill="none" stroke="#1e3260" stroke-width="1.4"/></svg></div>
      </li>
      <li class="player-row unselected">
        <div class="avatar" role="img" aria-label="Player portrait photo"></div><div class="coin">20</div>
        <div class="player-name">Jonas Brandt</div><div class="ranking">World Ranking: 42</div><div class="stats-link">Player Statistics</div>
        <svg class="flag" width="13" height="8" viewBox="0 0 13 8"><rect width="13" height="8" fill="var(--flag-blue)"/><rect x="4" width="2" height="8" fill="var(--flag-yellow)"/><rect y="3" width="13" height="2" fill="var(--flag-yellow)"/></svg>
        <div class="checkbox"><svg width="7" height="6" viewBox="0 0 7 6"><path d="M1 3l2 2 3-4" fill="none" stroke="#9aa0b0" stroke-width="1.4"/></svg></div>
      </li>
      <li class="player-row selected">
        <div class="avatar" role="img" aria-label="Player portrait photo"></div><div class="coin">20</div>
        <div class="player-name">Ben Carver</div><div class="ranking">World Ranking: 42</div><div class="stats-link">Player Statistics</div>
        <svg class="flag" width="13" height="8" viewBox="0 0 13 8"><rect width="13" height="8" fill="var(--flag-blue)"/><rect x="4" width="2" height="8" fill="var(--flag-yellow)"/><rect y="3" width="13" height="2" fill="var(--flag-yellow)"/></svg>
        <div class="checkbox"><svg width="7" height="6" viewBox="0 0 7 6"><path d="M1 3l2 2 3-4" fill="none" stroke="#1e3260" stroke-width="1.4"/></svg></div>
      </li>
      <li class="player-row unselected">
        <div class="avatar" role="img" aria-label="Player portrait photo"></div><div class="coin">20</div>
        <div class="player-name">Mats Wilde</div><div class="ranking">World Ranking: 42</div><div class="stats-link">Player Statistics</div>
        <svg class="flag" width="13" height="8" viewBox="0 0 13 8"><rect width="13" height="8" fill="var(--flag-blue)"/><rect x="4" width="2" height="8" fill="var(--flag-yellow)"/><rect y="3" width="13" height="2" fill="var(--flag-yellow)"/></svg>
        <div class="checkbox"><svg width="7" height="6" viewBox="0 0 7 6"><path d="M1 3l2 2 3-4" fill="none" stroke="#9aa0b0" stroke-width="1.4"/></svg></div>
      </li>
      <li class="player-row unselected">
        <div class="avatar" role="img" aria-label="Player portrait photo"></div><div class="coin">20</div>
        <div class="player-name">Bram van Dorne</div><div class="ranking">World Ranking: 42</div><div class="stats-link">Player Statistics</div>
        <svg class="flag" width="13" height="8" viewBox="0 0 13 8"><rect width="13" height="8" fill="var(--flag-blue)"/><rect x="4" width="2" height="8" fill="var(--flag-yellow)"/><rect y="3" width="13" height="2" fill="var(--flag-yellow)"/></svg>
        <div class="checkbox"><svg width="7" height="6" viewBox="0 0 7 6"><path d="M1 3l2 2 3-4" fill="none" stroke="#9aa0b0" stroke-width="1.4"/></svg></div>
      </li>
    </ul>
    <div class="scrollbar"></div>

    <div class="panel-actions">
      <div class="btn clear">Clear</div>
      <div class="btn next">Next Choose Winner</div>
    </div>
  </section>

  <nav class="tab-bar">
    <div class="tab">
      <svg width="22" height="9" viewBox="0 0 22 9"><g fill="#fff"><circle cx="4" cy="2.5" r="2"/><path d="M0 9a4 4 0 0 1 8 0z"/><circle cx="11" cy="2.5" r="2"/><path d="M7 9a4 4 0 0 1 8 0z"/><circle cx="18" cy="2.5" r="2"/><path d="M14 9a4 4 0 0 1 8 0z"/></g></svg>
      Pick Players
    </div>
    <div class="tab">
      <svg width="10" height="9" viewBox="0 0 10 9"><path d="M0 4h2v5H0zM3 4l2-4c1 0 1.5.6 1.3 1.8L6 3.5h3.2c.6 0 1 .6.8 1.2L9 8.3c-.2.4-.5.7-1 .7H3z" fill="#fff"/></svg>
      My Beacon
    </div>
    <div class="tab">
      <svg width="12" height="8" viewBox="0 0 12 8"><path d="M3 0h6a3 3 0 0 1 3 3v2a2.5 2.5 0 0 1-4.3 1.8L7 6H5l-.7.8A2.5 2.5 0 0 1 0 5V3a3 3 0 0 1 3-3z" fill="#fff"/><rect x="2.5" y="2.5" width="3" height="1" fill="#2a3e70"/><rect x="3.5" y="1.5" width="1" height="3" fill="#2a3e70"/><circle cx="8.5" cy="3" r=".8" fill="#2a3e70"/></svg>
      My Games
    </div>
    <div class="tab">
      <svg width="8" height="9" viewBox="0 0 8 9"><circle cx="4" cy="2.3" r="2.2" fill="#fff"/><path d="M0 9a4 4 0 0 1 8 0z" fill="#fff"/></svg>
      My Profile
    </div>
  </nav>
</main>
</body>
</html>
```